Our architectural studio needs a new business card

We need a business card design for our studio based in Waterloo in Belgium. We are active in architecture, design and installation.
Our works are contemporary and minimalist. our clients are refined and cultured.
Our business card must be minimalist and refined.

Project Deadline Extended
Reason: Some designers have accepted my invitation but they don't have all replied. I want to give them a chance to make one proposal. Paul

Target Market(s)

architecture

Industry/Entity Type

Business

Contact Information for Business Card

studio: paul dornevaux studio
paul dornevaux, architecte
M. +32 471 586 927
F. +322 619 4850
www.pauldornevaux-example.com
paul@pauldornevaux-example.com
14 rue des Marronniers
1420 Waterloo
Belgium

Font styles to use
Sans Serif

Requirements
Must have
• simple, minimalist, clear, elegant and chic! Black and white
Nice to have
• embossed logo, other format like a square for example
Should not have
• color, fantasy, curves, ...

```html
<!DOCTYPE html>
<html lang="en">
<head>
<meta charset="utf-8">
<title>Paul Dornevaux Studio — Business Card</title>
<link rel="stylesheet" href="https://fonts.googleapis.com/css2?family=Lato:wght@300;400;700;900&display=swap">
<style>
  :root {
    --backdrop: #e9e7e4;
    --card: #ffffff;
    --ink: #111111;
    --ink-soft: #5a5a5a;
    --ink-muted: #8a8a8a;
    --edge: #d6d4d1;
  }
  * { box-sizing: border-box; margin: 0; padding: 0; }
  html, body {
    width: 1200px;
    height: 913px;
    overflow: hidden;
    background: var(--backdrop);
    font-family: "Lato", sans-serif;
    color: var(--ink);
  }
  .canvas {
    position: relative;
    width: 1200px;
    height: 913px;
  }
  .card {
    position: absolute;
    width: 525px;
    height: 300px;
    background: var(--card);
    border-radius: 20px;
    border: 1px solid var(--edge);
  }
  .card--front { left: 80px; top: 110px; }
  .card--back  { left: 595px; top: 500px; }

  /* Front */
  .front-mark {
    position: absolute;
    left: 50%;
    top: 78px;
    transform: translateX(-50%);
    display: flex;
    flex-direction: column;
    align-items: center;
    gap: 30px;
  }
  .mark-square {
    display: block;
    width: 58px;
    height: 58px;
    background: var(--ink);
  }
  .studio-name {
    font-weight: 700;
    font-size: 13px;
    letter-spacing: 0.32em;
    text-transform: uppercase;
    white-space: nowrap;
    color: var(--ink);
  }

  /* Back */
  .back-mark {
    position: absolute;
    left: 44px;
    top: 130px;
    display: flex;
    flex-direction: column;
    align-items: flex-start;
    gap: 14px;
  }
  .back-mark .mark-square { width: 58px; height: 58px; }
  .back-mark .studio-name { font-size: 10px; letter-spacing: 0.22em; }

  .contact {
    position: absolute;
    right: 26px;
    top: 42px;
    width: 232px;
    font-style: normal;
    font-size: 12px;
    line-height: 1.35;
    color: var(--ink-muted);
  }
  .contact__name {
    font-size: 15px;
    font-weight: 700;
    color: var(--ink-soft);
  }
  .contact__role { font-weight: 300; margin-bottom: 16px; }
  .contact__address { font-weight: 300; margin-bottom: 16px; }
  .contact__lines { list-style: none; }
  .contact__lines li { white-space: nowrap; font-weight: 400; }
  .contact__label {
    display: inline-block;
    width: 32px;
    font-weight: 700;
    color: var(--ink);
  }
</style>
</head>
<body>
<main class="canvas">
  <section class="card card--front" aria-label="Business card, front">
    <div class="front-mark">
      <span class="mark-square" aria-hidden="true"></span>
      <p class="studio-name">paul dornevaux studio</p>
    </div>
  </section>

  <section class="card card--back" aria-label="Business card, back">
    <div class="back-mark">
      <span class="mark-square" aria-hidden="true"></span>
      <p class="studio-name">paul dornevaux studio</p>
    </div>

    <address class="contact">
      <p class="contact__name">Paul Dornevaux Studio</p>
      <p class="contact__role">Architecte</p>
      <p class="contact__address">14 rue des Marronniers 1420<br>Waterloo Belgium</p>
      <ul class="contact__lines">
        <li><span class="contact__label">(M) :</span>+32 471 586 927</li>
        <li><span class="contact__label">(F) :</span>+322 619 4850</li>
        <li><span class="contact__label">(E) :</span>www.pauldornevaux-example.com</li>
        <li><span class="contact__label">(W):</span>paul@pauldornevaux-example.com</li>
      </ul>
    </address>
  </section>
</main>
</body>
</html>
```